Postcard needed for expert witness service

Looking for a professional postcard that will be mailed to personal injury lawyers / law firms to introduce my expert witness services.

Target Market(s)

Law firms, personal injury lawyers

Industry/Entity Type

Expert witness, law

Font styles to use
Sans Serif

Requirements
Must have
• Logo: The Frost Counsel [Main Heading]Do you handle snow and ice related slip and falls? Darrel is one of the top snow industry experts in the country! [Following should be in a list type fashion, possibly bulleted]Darrel's credentials: Accredited Winter Practitioner (AWP), past WRTA board member and chair, former ISO 9001 certified snow company owner , 32 years in the industry. (555) 284-3917 NOTES: Postcard will be 4" x 6" Please use both sides however must have room for labels and stamp
Should not have
• Wouldn't suggest using both photos on same side. Honestly, feel free to only use one of the slip and fall photos if it works out better. Thanks!

```html
<!DOCTYPE html>
<html lang="en">
<head>
<meta charset="utf-8">
<title>The Frost Counsel – Postcard</title>
<link href="https://fonts.googleapis.com/css2?family=Arimo:wght@400;500&display=swap" rel="stylesheet">
<style>
  :root {
    --orange: #e8711a;
    --orange-dark: #b5520f;
    --blue: #0f5aa6;
    --blue-text: #2a5bd7;
    --ink: #1b1b1b;
    --white: #ffffff;
    --stage: #ececec;
    --rule: #d6d6d6;
    --stamp: #e3e3e3;
  }
  * { margin: 0; padding: 0; box-sizing: border-box; }
  html, body {
    width: 685px; height: 1200px; overflow: hidden;
    background: var(--stage);
    font-family: "Arimo", Arial, sans-serif;
    color: var(--ink);
  }
  .postcard {
    position: absolute; left: 42px; width: 600px; height: 400px;
    background: var(--white); overflow: hidden;
    box-shadow: 0 2px 8px rgba(0,0,0,.12);
  }
  .postcard--front { top: 170px; }
  .postcard--back { top: 630px; }
  .shapes { position: absolute; inset: 0; }

  /* front */
  .brand { position: absolute; left: 26px; top: 30px; color: var(--ink); font-weight: 400; }
  .brand__name { font-size: 33px; line-height: 1; letter-spacing: .5px; }
  .brand__sub { font-size: 15px; letter-spacing: 6px; margin-top: 3px; padding-left: 48px; }
  .headline {
    position: absolute; left: 26px; top: 150px; width: 300px;
    color: var(--white); font-size: 38px; line-height: 1.04; font-weight: 400;
  }
  .contact-row {
    position: absolute; left: 24px; bottom: 15px;
    display: flex; gap: 14px; align-items: center;
    color: var(--white); font-size: 14px;
  }
  .contact-row span { display: flex; align-items: center; gap: 6px; }
  .icon { width: 18px; height: 18px; fill: none; stroke: currentColor; stroke-width: 1.4; }
  .icon--orange { color: var(--orange); }

  /* back */
  .intro { position: absolute; left: 31px; top: 24px; }
  .intro__lead { font-size: 11px; letter-spacing: .2px; }
  .intro__title { color: var(--blue-text); font-size: 25px; line-height: 1.2; margin-top: 4px; }
  .intro__tail { font-size: 15px; margin-top: 2px; }
  .photo-back {
    position: absolute; left: 0; top: 124px; width: 358px; height: 237px;
    background: linear-gradient(120deg, #c9ccd2 0%, #46597e 35%, #7d6a5a 60%, #d4d3d0 100%);
  }
  .credentials {
    position: absolute; left: 161px; top: 143px; width: 187px; height: 186px;
    background: var(--orange); color: var(--white);
    border-radius: 14px 0 14px 0; padding: 14px 14px 0 15px;
  }
  .credentials__title { font-size: 13px; margin-bottom: 9px; }
  .credentials__list { list-style: none; }
  .credentials__list li {
    display: flex; gap: 6px; font-size: 10.5px; line-height: 1.25; margin-bottom: 9px;
  }
  .credentials__list svg { width: 10px; height: 10px; flex: none; margin-top: 1px; fill: none; stroke: var(--white); stroke-width: 1.2; }
  .brand--small { left: 402px; top: 54px; }
  .brand--small .brand__name { font-size: 13px; }
  .brand--small .brand__sub { font-size: 6px; letter-spacing: 2.4px; padding-left: 17px; margin-top: 1px; }
  .stamp { position: absolute; left: 514px; top: 34px; width: 52px; height: 52px; background: var(--stamp); }
  .address-line { position: absolute; left: 396px; width: 170px; height: 1px; background: var(--rule); }
  .band {
    position: absolute; left: 0; bottom: 0; width: 100%; height: 39px;
    background: var(--blue); color: var(--white); font-size: 13px;
    display: flex; align-items: center; justify-content: space-around; padding: 0 40px;
  }
  .band span { display: flex; align-items: center; gap: 8px; }
  .band .icon { width: 14px; height: 14px; }
</style>
</head>
<body>

<section class="postcard postcard--front">
  <svg class="shapes" viewBox="0 0 600 400" width="600" height="400">
    <defs>
      <linearGradient id="frontPhotoTone" x1="0" y1="0" x2="1" y2="1">
        <stop offset="0" stop-color="#e2e0dc"/>
        <stop offset=".45" stop-color="#7a6a60"/>
        <stop offset=".75" stop-color="#4d5f7c"/>
        <stop offset="1" stop-color="#c8c4bd"/>
      </linearGradient>
    </defs>
    <polygon role="img" aria-label="Photo of a woman in a winter hat who has slipped and fallen on an icy, snowy pavement" points="315,0 600,0 600,282 280,282 280,119" fill="url(#frontPhotoTone)"/>
    <polygon points="408,282 600,282 600,293 582,293 494,400 0,400 0,346" fill="var(--blue)"/>
    <polygon points="0,119 296,119 453,346 0,346" fill="var(--orange)"/>
    <polygon points="408,282 468,293 453,346" fill="var(--orange-dark)"/>
    <polygon points="582,293 600,293 600,400 494,400" fill="var(--white)"/>
    <polygon points="542,362 600,362 600,386 526,386" fill="var(--orange)"/>
  </svg>

  <div class="brand">
    <div class="brand__name">THE FROST</div>
    <div class="brand__sub">COUNSEL</div>
  </div>

  <h1 class="headline">Do you handle snow and ice related slip and falls?</h1>

  <div class="contact-row">
    <span><svg class="icon icon--orange" viewBox="0 0 24 24"><path d="M5 3l4 1 1 5-2 1a11 11 0 0 0 6 6l1-2 5 1 1 4-3 2C10 21 3 14 3 6z"/></svg>(555) 284-3917</span>
    <span><svg class="icon icon--orange" viewBox="0 0 24 24"><rect x="3" y="6" width="18" height="12"/><path d="M3 6l9 7 9-7"/></svg>@frostcounselmail.com</span>
    <span><svg class="icon icon--orange" viewBox="0 0 24 24"><circle cx="12" cy="12" r="9"/><path d="M3 12h18M12 3c3 3 3 15 0 18M12 3c-3 3-3 15 0 18"/></svg>www.frostcounsel.net</span>
  </div>
</section>

<section class="postcard postcard--back">
  <div class="intro">
    <p class="intro__lead">DARREL IS ONE OF THE TOP</p>
    <h2 class="intro__title">SNOW INDUSTRY<br>EXPERTS</h2>
    <p class="intro__tail">IN THE COUNTRY!</p>
  </div>

  <div class="photo-back" role="img" aria-label="Photo of a person slipping backwards on a wet, icy street with a bag falling beside them"></div>

  <div class="credentials">
    <p class="credentials__title">Darrel's credentials:</p>
    <ul class="credentials__list">
      <li><svg viewBox="0 0 12 12"><circle cx="6" cy="6" r="5"/><path d="M3.5 6l2 2 3-4"/></svg>Accredited Winter<br>Practitioner (AWP)</li>
      <li><svg viewBox="0 0 12 12"><circle cx="6" cy="6" r="5"/><path d="M3.5 6l2 2 3-4"/></svg>Former ISO 9001 certified<br>snow company owner</li>
      <li><svg viewBox="0 0 12 12"><circle cx="6" cy="6" r="5"/><path d="M3.5 6l2 2 3-4"/></svg>Past WRTA board<br>member and chair</li>
      <li><svg viewBox="0 0 12 12"><circle cx="6" cy="6" r="5"/><path d="M3.5 6l2 2 3-4"/></svg>32 years in<br>the industry</li>
    </ul>
  </div>

  <div class="brand brand--small">
    <div class="brand__name">THE FROST</div>
    <div class="brand__sub">COUNSEL</div>
  </div>
  <div class="stamp"></div>
  <div class="address-line" style="top:168px"></div>
  <div class="address-line" style="top:196px"></div>
  <div class="address-line" style="top:224px"></div>

  <div class="band">
    <span><svg class="icon" viewBox="0 0 24 24"><path d="M5 3l4 1 1 5-2 1a11 11 0 0 0 6 6l1-2 5 1 1 4-3 2C10 21 3 14 3 6z"/></svg>(555) 284-3917</span>
    <span><svg class="icon" viewBox="0 0 24 24"><rect x="3" y="6" width="18" height="12"/><path d="M3 6l9 7 9-7"/></svg>@frostcounselmail.com</span>
    <span><svg class="icon" viewBox="0 0 24 24"><circle cx="12" cy="12" r="9"/><path d="M3 12h18M12 3c3 3 3 15 0 18M12 3c-3 3-3 15 0 18"/></svg>www.frostcounsel.net</span>
  </div>
</section>

</body>
</html>
```